Bluewater Getaways KT needs a new Website

We have an old website that is just that - old. We need a fresh website that is professional graphic designed that has the following features.
1. Can be updated by ourselves in some areas.
2. Has a shopping cart.
3. Has links to download PDF files
4. Has links to other pages in the website
5. Includes social media links
6. Has a client log-in area
Full details in brief provided.

SORRY BUT IT'S URGENT. We've taken too long to write the details and it is now urgent. So my apologies I will be asking for designers to work quickly.

We will continue to use our existing web hosting company and url. Their is a link to the old website in the Design Brief.
Updates

UPDATE:  Please see the new file UPDATE TO DESIGN BRIEF.
Thanks for all your submissions to date.  We hope the update will assist with your designs.
As indicated in previous messages, we are happy with the Home Page + 1 Page in order to select the designer to work with in creating the full design. 

Thankyou Designers.  Much appreciate your efforts.
It's getting late here on Norfolk so I won't have much chance too review any more designs this evening.
But for your information:
Designer 7318405 Ravindra Mehta is so far the closest to what we are seeking.
Thanks again. 

Reason: Have extended to Monday 7 October to give time for designers to submit after feedback today. Especially given the time differences

Target Market(s)

Very wide audience. Current client group not that tech savvy, but we hope to broaden our market and sell more creative products, and so website needs to consider how people now use media, ie tablets & iphones.

Industry/Entity Type

Shopping

Requirements
Nice to have
• PLEASE SEE THE "UPDATE TO THE DESIGN BRIEF"

```html
<!DOCTYPE html>
<html lang="en">
<head>
<meta charset="utf-8">
<title>Bluewater Getaways KT</title>
<link rel="stylesheet" href="https://fonts.googleapis.com/css2?family=Open+Sans:ital,wght@0,400;0,600;1,700&family=Zilla+Slab:wght@300;400&display=swap">
<style>
  :root {
    --sepia-mid: #b59c7c;
    --sepia-light: #e9d4b6;
    --sand: #f6e6cf;
    --white: #ffffff;
    --ink: #111111;
    --chip: rgba(150, 150, 150, 0.75);
    --badge: rgba(90, 80, 70, 0.65);
    --badge-text: #c9c2b8;
    --nav-band: rgba(255, 255, 255, 0.18);
    --nav-active: #e9dcc6;
  }
  * { box-sizing: border-box; margin: 0; padding: 0; }
  html, body { width: 1200px; height: 640px; overflow: hidden; background: var(--white); }
  body { font-family: "Open Sans", sans-serif; color: var(--white); position: relative; }

  .hero-photo {
    position: absolute; inset: 0;
    background:
      radial-gradient(ellipse 40% 45% at 20% 55%, rgba(233, 212, 182, 0.9), transparent 70%),
      radial-gradient(ellipse 35% 50% at 70% 25%, rgba(60, 48, 36, 0.85), transparent 70%),
      radial-gradient(ellipse 30% 45% at 95% 20%, rgba(50, 40, 30, 0.9), transparent 70%),
      radial-gradient(ellipse 25% 40% at 5% 30%, rgba(90, 75, 55, 0.8), transparent 70%),
      linear-gradient(180deg, var(--sepia-mid) 0%, var(--sepia-light) 55%, var(--sand) 78%, var(--white) 97%);
  }

  .site-header { position: absolute; left: 0; top: 0; width: 1200px; height: 120px; }
  .brand {
    position: absolute; left: 155px; top: 32px;
    font-family: "Open Sans", sans-serif; font-weight: 600; font-size: 17px; line-height: 20px;
    color: var(--white); text-transform: uppercase; white-space: nowrap;
  }

  .account-links {
    position: absolute; right: 153px; top: 21px; display: flex; gap: 14px;
    font-size: 11.5px; color: var(--white);
  }
  .account-links svg { vertical-align: -1px; margin-right: 3px; }

  .utility-bar { position: absolute; right: 153px; top: 44px; display: flex; align-items: center; gap: 5px; }
  .chip {
    background: var(--chip); color: var(--white); font-size: 9.5px; text-transform: uppercase;
    height: 18px; line-height: 18px; padding: 0 10px; border-radius: 2px;
  }
  .social { font-size: 11px; font-weight: 600; margin-left: 6px; color: var(--white); }

  .main-nav {
    position: absolute; left: 32px; top: 87px; width: 1136px; height: 32px;
    background: var(--nav-band);
  }
  .main-nav a {
    position: absolute; top: 6px; font-family: "Zilla Slab", serif; font-size: 16px;
    color: var(--white); text-decoration: none; text-transform: uppercase; white-space: nowrap;
  }
  .main-nav a.is-current { color: var(--nav-active); opacity: 0.8; }

  .hero-copy { position: absolute; left: 152px; top: 235px; }
  .est-badge {
    display: inline-block; margin-left: 3px; height: 19px; line-height: 19px; padding: 0 16px 0 7px;
    background: var(--badge); color: var(--badge-text); font-size: 9.5px; font-weight: 700;
    font-style: italic; text-transform: uppercase; border-radius: 2px;
  }
  .hero-title {
    font-family: "Zilla Slab", serif; font-weight: 300; font-size: 50px; line-height: 48px;
    margin-top: 6px; text-transform: uppercase; white-space: nowrap;
  }
  .hero-sub {
    font-family: "Zilla Slab", serif; font-weight: 300; font-size: 40px; line-height: 40px;
    white-space: nowrap;
  }
  .cta {
    position: absolute; left: 176px; top: 130px; width: 155px; height: 33px;
    background: var(--ink); color: var(--white); border-radius: 4px; text-align: center;
    font-family: "Zilla Slab", serif; font-size: 21px; line-height: 33px; text-decoration: none;
  }

  .site-footer {
    position: absolute; left: 0; top: 560px; width: 1200px; text-align: center;
    color: var(--ink); font-size: 11.5px; line-height: 20px;
  }
</style>
</head>
<body>
  <div class="hero-photo" role="img" aria-label="Soft sepia photograph of a couple walking along a beach lined with tall pine trees"></div>

  <header class="site-header">
    <div class="brand">Bluewater Getaways KT</div>

    <nav class="account-links">
      <span><svg width="11" height="9" viewBox="0 0 11 9"><path d="M0 1h2l1.5 5h6L11 2H3" fill="none" stroke="#fff" stroke-width="1.3"/><circle cx="4" cy="8" r="1" fill="#fff"/><circle cx="9" cy="8" r="1" fill="#fff"/></svg>My Cart</span>
      <span>Create an Account</span>
      <span>Sign In</span>
    </nav>

    <div class="utility-bar">
      <span class="chip">Download PDF files</span>
      <span class="chip">Social share</span>
      <span class="social">Like</span>
      <span class="social">Follow</span>
    </div>

    <nav class="main-nav">
      <a style="left:142px">Home</a>
      <a style="left:222px">Overview</a>
      <a style="left:336px">Kestrel Isle</a>
      <a class="is-current" style="left:499px">Services</a>
      <a style="left:607px">Our Shop</a>
      <a style="left:725px">Make a Booking</a>
      <a style="left:893px">Testimonials</a>
    </nav>
  </header>

  <section class="hero-copy">
    <span class="est-badge">Established July 2001</span>
    <h1 class="hero-title">Lorem Ipsum</h1>
    <p class="hero-sub">Bluewater Getaway</p>
    <a class="cta">Call to Action</a>
  </section>

  <footer class="site-footer">
    <p>About Us | Contact Us | Terms &amp; Condition &nbsp;| &nbsp;Privacy Policy Copyright © 2013 Bluewater Getaways KT. All rights reserved</p>
    <p>International + 64 55 01937 &nbsp;&nbsp;| &nbsp;&nbsp;Australia 1800 555 014</p>
  </footer>
</body>
</html>
```